Heavy Duty Repairs Poster

Good afternoon - I'm looking for a poster , design to set up around different areas. The Poster must consist of the following
- Heavy duty repairs
- Pictures of Semi trucks , heavy construction equipment , trailers
- Agriculture
- All north American equipment ( see attached pictures)
- Brief Descriptions in bullet point forms
CVIPS
WELDING
AIR CONDITIONING
ENGINE REBUILDS
DIAGONSTICS
FLEET MANAGMENT
TIRE REPAIR AND SALES
ELECTRICAL , HYDRALIC , POWER TRAIN SERVICE AND REPAIRS
PART SALES
FLEET MAINTINACE
DELTEING AND TUNING
AFTER MARKET INSTALLS OUTFITTING
ONSITE & OFFSITE REPAIRS
FULL RECERTIFACTION OVERHAULING
Warranty Approved

Target Market(s)

Heavy Duty Truck , Equipment , Agriculture Owners

Industry/Entity Type

Heavy Duty Repairs

Colors
EB3D1F
EC4F4E
F09395
F8D3D4
FCEDEE

Requirements
Must have
• Pictures of : Semi trucks and trailer , Construction heavy equipment , agriculture equipment
Nice to have
• Flashy and stands out

```html
<!DOCTYPE html>
<html lang="en">
<head>
<meta charset="utf-8">
<title>Ridge Mechanical Services Poster</title>
<link href="https://fonts.googleapis.com/css2?family=Oswald:wght@400;500;700&family=Montserrat:wght@500;700;800&display=swap" rel="stylesheet">
<style>
  :root {
    --red: #eb3d1f;
    --red-deep: #d4141c;
    --rose: #ec4f4e;
    --pink: #f09395;
    --blush: #f8d3d4;
    --mist: #fcedee;
    --ink: #1a1a1a;
    --black: #151515;
    --silver: #e4e6ea;
    --steel: #9aa0a8;
    --page: #d9d9d9;
    --panel: #f1f1f1;
    --white: #ffffff;
  }
  * { margin: 0; padding: 0; box-sizing: border-box; }
  html, body { width: 750px; height: 1200px; overflow: hidden; background: var(--page); }
  .poster {
    position: absolute; left: 25px; top: 100px; width: 700px; height: 1001px;
    background: var(--panel);
    overflow: hidden; box-shadow: 0 14px 30px rgba(0,0,0,0.25);
  }
  .hero-photo {
    position: absolute; left: 0; top: 0; width: 700px; height: 485px; z-index: 0;
    background:
      radial-gradient(ellipse 170px 260px at 350px 200px, rgba(40,18,18,0.75) 0%, rgba(40,18,18,0) 100%),
      linear-gradient(180deg, #8fa7c2 0%, #c9c9d2 30%, #c77070 55%, #8a3a2a 72%, #4a2018 100%);
  }
  .field-photo {
    position: absolute; left: 0; top: 700px; width: 700px; height: 220px; z-index: 0;
    background: linear-gradient(180deg, var(--panel) 0%, #d6ddd4 18%, #b9b3a3 45%, #8d7f6c 100%);
  }
  .shapes { position: absolute; left: 0; top: 0; z-index: 1; }
  .brand-title {
    position: absolute; left: 0; width: 700px; top: 245px; text-align: center; z-index: 2;
    font-family: "Oswald", sans-serif; font-weight: 700; color: var(--silver);
    font-size: 112px; line-height: 1; letter-spacing: 2px;
  }
  .brand-tagline {
    position: absolute; left: 0; width: 700px; top: 370px; text-align: center; z-index: 2;
    font-family: "Oswald", sans-serif; font-weight: 700; color: var(--silver);
    font-size: 31px; letter-spacing: 1.5px;
  }
  .service-column { position: absolute; top: 496px; list-style: none; z-index: 3; }
  .service-column.col-a { left: 46px; }
  .service-column.col-b { left: 240px; }
  .service-column.col-c { left: 464px; }
  .service-item {
    display: flex; align-items: flex-start; gap: 8px;
    font-family: "Oswald", sans-serif; font-weight: 500; font-size: 17px;
    line-height: 24px; color: var(--ink); margin-bottom: 13px; text-transform: uppercase;
  }
  .tick { flex: none; margin-top: 4px; }
  .seal { position: absolute; left: 270px; top: 727px; z-index: 4; }
  .seal-word { font-family: "Oswald", sans-serif; text-anchor: middle; }
  .footer { position: absolute; left: 0; top: 895px; width: 700px; height: 106px; z-index: 3; }
  .contact-block { position: absolute; left: 40px; top: 14px; width: 195px; text-align: right; font-family: "Montserrat", sans-serif; color: var(--white); }
  .contact-heading { font-weight: 800; font-size: 13px; letter-spacing: 0.5px; margin-bottom: 8px; }
  .contact-line { font-weight: 500; font-size: 10.5px; line-height: 17px; display: flex; justify-content: flex-end; align-items: center; gap: 5px; white-space: nowrap; }
  .dot { width: 6px; height: 6px; background: var(--red-deep); border-radius: 50%; flex: none; }
  .center-block { position: absolute; left: 250px; top: 12px; width: 200px; text-align: center; font-family: "Montserrat", sans-serif; }
  .center-phone { color: var(--red-deep); font-weight: 800; font-size: 17px; letter-spacing: 0.5px; }
  .center-name { color: var(--white); font-weight: 500; font-size: 11px; margin-top: 10px; }
  .center-place { color: var(--white); font-weight: 500; font-size: 9px; margin-top: 2px; }
  .call-block { position: absolute; left: 460px; top: 14px; font-family: "Montserrat", sans-serif; color: var(--white); }
  .call-heading { font-weight: 800; font-size: 13px; letter-spacing: 0.5px; margin-bottom: 6px; }
  .call-number { font-weight: 800; font-size: 24px; display: flex; align-items: center; gap: 6px; letter-spacing: 0.5px; }
</style>
</head>
<body>
  <main class="poster">
    <div class="hero-photo" role="img" aria-label="Red farm tractor driving across a ploughed field at sunset"></div>
    <div class="field-photo" role="img" aria-label="Yellow wheel loaders with buckets on open dirt ground, one on each side"></div>

    <svg class="shapes" width="700" height="1001" viewBox="0 0 700 1001" aria-hidden="true">
      <polygon points="0,399 350,457 700,399 700,420 350,483 0,420" fill="var(--red-deep)"/>
      <polygon points="0,420 350,483 700,420 700,702 0,702" fill="var(--panel)"/>
      <polygon points="0,940 260,848 440,848 700,940 700,1001 0,1001" fill="var(--black)"/>
      <polygon points="0,925 260,832 270,850 0,945" fill="var(--red-deep)"/>
      <polygon points="700,925 440,832 430,850 700,945" fill="var(--red-deep)"/>
      <rect x="0" y="920" width="700" height="81" fill="var(--black)"/>
    </svg>

    <h1 class="brand-title">RIDGE</h1>
    <p class="brand-tagline">MECHANICAL SERVICES</p>

    <ul class="service-column col-a">
      <li class="service-item"><svg class="tick" width="15" height="15" viewBox="0 0 16 16"><circle cx="8" cy="8" r="8" fill="var(--red-deep)"/><path d="M4.5 8.2l2.4 2.4 4.6-4.8" stroke="#fff" stroke-width="2" fill="none"/></svg>CVIPS</li>
      <li class="service-item"><svg class="tick" width="15" height="15" viewBox="0 0 16 16"><circle cx="8" cy="8" r="8" fill="var(--red-deep)"/><path d="M4.5 8.2l2.4 2.4 4.6-4.8" stroke="#fff" stroke-width="2" fill="none"/></svg>Welding</li>
      <li class="service-item"><svg class="tick" width="15" height="15" viewBox="0 0 16 16"><circle cx="8" cy="8" r="8" fill="var(--red-deep)"/><path d="M4.5 8.2l2.4 2.4 4.6-4.8" stroke="#fff" stroke-width="2" fill="none"/></svg>Air Conditioning</li>
      <li class="service-item"><svg class="tick" width="15" height="15" viewBox="0 0 16 16"><circle cx="8" cy="8" r="8" fill="var(--red-deep)"/><path d="M4.5 8.2l2.4 2.4 4.6-4.8" stroke="#fff" stroke-width="2" fill="none"/></svg>Engine Rebuilds</li>
      <li class="service-item"><svg class="tick" width="15" height="15" viewBox="0 0 16 16"><circle cx="8" cy="8" r="8" fill="var(--red-deep)"/><path d="M4.5 8.2l2.4 2.4 4.6-4.8" stroke="#fff" stroke-width="2" fill="none"/></svg>Diagonstics</li>
      <li class="service-item"><svg class="tick" width="15" height="15" viewBox="0 0 16 16"><circle cx="8" cy="8" r="8" fill="var(--red-deep)"/><path d="M4.5 8.2l2.4 2.4 4.6-4.8" stroke="#fff" stroke-width="2" fill="none"/></svg>Fleet Managment</li>
    </ul>
    <ul class="service-column col-b">
      <li class="service-item"><svg class="tick" width="15" height="15" viewBox="0 0 16 16"><circle cx="8" cy="8" r="8" fill="var(--red-deep)"/><path d="M4.5 8.2l2.4 2.4 4.6-4.8" stroke="#fff" stroke-width="2" fill="none"/></svg>Tire Repair and Sales</li>
      <li class="service-item"><svg class="tick" width="15" height="15" viewBox="0 0 16 16"><circle cx="8" cy="8" r="8" fill="var(--red-deep)"/><path d="M4.5 8.2l2.4 2.4 4.6-4.8" stroke="#fff" stroke-width="2" fill="none"/></svg>Electrical</li>
      <li class="service-item"><svg class="tick" width="15" height="15" viewBox="0 0 16 16"><circle cx="8" cy="8" r="8" fill="var(--red-deep)"/><path d="M4.5 8.2l2.4 2.4 4.6-4.8" stroke="#fff" stroke-width="2" fill="none"/></svg>Hydralic</li>
      <li class="service-item"><svg class="tick" width="15" height="15" viewBox="0 0 16 16"><circle cx="8" cy="8" r="8" fill="var(--red-deep)"/><path d="M4.5 8.2l2.4 2.4 4.6-4.8" stroke="#fff" stroke-width="2" fill="none"/></svg>Power Train Service<br>and Repairs</li>
      <li class="service-item"><svg class="tick" width="15" height="15" viewBox="0 0 16 16"><circle cx="8" cy="8" r="8" fill="var(--red-deep)"/><path d="M4.5 8.2l2.4 2.4 4.6-4.8" stroke="#fff" stroke-width="2" fill="none"/></svg>Part Sales</li>
    </ul>
    <ul class="service-column col-c">
      <li class="service-item"><svg class="tick" width="15" height="15" viewBox="0 0 16 16"><circle cx="8" cy="8" r="8" fill="var(--red)"/><path d="M4.5 8.2l2.4 2.4 4.6-4.8" stroke="#fff" stroke-width="2" fill="none"/></svg>Fleet Maintinace</li>
      <li class="service-item"><svg class="tick" width="15" height="15" viewBox="0 0 16 16"><circle cx="8" cy="8" r="8" fill="var(--red)"/><path d="M4.5 8.2l2.4 2.4 4.6-4.8" stroke="#fff" stroke-width="2" fill="none"/></svg>Delteing and Tuning</li>
      <li class="service-item"><svg class="tick" width="15" height="15" viewBox="0 0 16 16"><circle cx="8" cy="8" r="8" fill="var(--red)"/><path d="M4.5 8.2l2.4 2.4 4.6-4.8" stroke="#fff" stroke-width="2" fill="none"/></svg>After Market Installs<br>Outfitting</li>
      <li class="service-item"><svg class="tick" width="15" height="15" viewBox="0 0 16 16"><circle cx="8" cy="8" r="8" fill="var(--red)"/><path d="M4.5 8.2l2.4 2.4 4.6-4.8" stroke="#fff" stroke-width="2" fill="none"/></svg>Onsite &amp; Offsite Repairs</li>
      <li class="service-item"><svg class="tick" width="15" height="15" viewBox="0 0 16 16"><circle cx="8" cy="8" r="8" fill="var(--red)"/><path d="M4.5 8.2l2.4 2.4 4.6-4.8" stroke="#fff" stroke-width="2" fill="none"/></svg>Full Recertifaction<br>Overhauling</li>
    </ul>

    <svg class="seal" width="160" height="160" viewBox="0 0 160 160" role="img" aria-label="Warranty approved seal">
      <defs>
        <radialGradient id="seal-metal" cx="40%" cy="35%" r="70%">
          <stop offset="0%" stop-color="#ffffff"/>
          <stop offset="60%" stop-color="#c9ccd1"/>
          <stop offset="100%" stop-color="#8e939a"/>
        </radialGradient>
        <radialGradient id="seal-face" cx="50%" cy="40%" r="65%">
          <stop offset="0%" stop-color="#ffffff"/>
          <stop offset="100%" stop-color="#dcdfe3"/>
        </radialGradient>
      </defs>
      <circle cx="80" cy="80" r="78" fill="url(#seal-metal)"/>
      <circle cx="80" cy="80" r="64" fill="url(#seal-face)" stroke="#6f747b" stroke-width="2"/>
      <line x1="46" y1="44" x2="114" y2="44" stroke="#444" stroke-width="2"/>
      <rect x="34" y="56" width="92" height="24" fill="var(--red-deep)"/>
      <text class="seal-word" x="80" y="75" font-size="19" font-weight="500" fill="#ffffff">WARRANTY</text>
      <text class="seal-word" x="80" y="104" font-size="25" font-weight="500" fill="#2a2a2a">APPROVED</text>
      <line x1="46" y1="112" x2="114" y2="112" stroke="#444" stroke-width="2"/>
      <text class="seal-word" x="80" y="126" font-size="10" fill="#2a2a2a">★ ★ ★</text>
    </svg>

    <footer class="footer">
      <div class="contact-block">
        <p class="contact-heading">CONTACT US</p>
        <p class="contact-line"><span class="dot"></span>info@ridgemechanical.example</p>
        <p class="contact-line"><span class="dot"></span>www.ridgemechanical.example</p>
      </div>
      <div class="center-block">
        <p class="center-phone">555-014-2694</p>
        <p class="center-name">Ridge Mechanical Services</p>
        <p class="center-place">Carrow Flats, Alberta</p>
      </div>
      <div class="call-block">
        <p class="call-heading">CALL US NOW!</p>
        <p class="call-number">
          <svg width="18" height="18" viewBox="0 0 24 24" aria-hidden="true"><path d="M6.6 10.8a15 15 0 0 0 6.6 6.6l2.2-2.2c.3-.3.7-.4 1-.2 1.1.4 2.3.6 3.6.6.6 0 1 .4 1 1V20c0 .6-.4 1-1 1A17 17 0 0 1 3 4c0-.6.4-1 1-1h3.5c.6 0 1 .4 1 1 0 1.3.2 2.5.6 3.6.1.3 0 .7-.2 1z" fill="var(--red-deep)"/></svg>
          555 0147575
        </p>
      </div>
    </footer>
  </main>
</body>
</html>
```